Aged Care Consultancy Business needs a business card design

I need a two sided business card - I want it clean and professional. Surprise me

Target Market(s)

middle aged and ageing victorians

Industry/Entity Type

Health Care

Contact Information for Business Card

Text to be included

Logo
Aged Care Consulting Services
Professional, Reliable, Affordable

Tovan Brelsick
Director
0427 31 64 92 (larger)
1300 73 29 41
tovan@wadolire.com.au
www.wadolcare.com.au
Facebook (details TBA)

include little icons beside the contact info:

- Envelope = email
- Phone = phone
- Globe = website

Font styles to use
Serif
Sans Serif

Requirements
Must have
• look proffesional and clean

```html
<!DOCTYPE html>
<html lang="en">
<head>
<meta charset="utf-8">
<title>Wadol Care – Business Card</title>
<link href="https://fonts.googleapis.com/css2?family=Catamaran:wght@700&family=Questrial&display=swap" rel="stylesheet">
<style>
  :root {
    --backdrop: #b1b1b1;
    --card-light: #f4f4f4;
    --card-light-edge: #e3e3e3;
    --navy: #1f3f76;
    --navy-deep: #1b3a6e;
    --orange: #e68a1e;
    --white: #ffffff;
    --soft-white: #e6ebf3;
  }
  * { box-sizing: border-box; margin: 0; padding: 0; }
  html, body {
    width: 1200px; height: 1050px; overflow: hidden;
    background: var(--backdrop);
  }
  .canvas { position: relative; width: 1200px; height: 1050px; }
  .card {
    position: absolute; left: 264px; width: 672px; height: 383px;
    box-shadow: 0 3px 8px rgba(0,0,0,.35);
    font-family: "Questrial", "Century Gothic", sans-serif;
  }
  .card--front {
    top: 111px;
    background: radial-gradient(ellipse at 55% 30%, #fbfbfb 0%, var(--card-light) 45%, var(--card-light-edge) 100%);
    color: var(--navy);
  }
  .card--back {
    top: 574px;
    background: radial-gradient(ellipse at 50% 45%, #1f4680 0%, var(--navy-deep) 70%, #183565 100%);
    color: var(--white);
  }
  .brand {
    position: absolute; display: flex; align-items: center; gap: 12px;
    font-family: "Catamaran", sans-serif; font-weight: 700; line-height: 1;
    white-space: nowrap;
  }
  .brand__dot { border-radius: 50%; background: var(--orange); flex: none; }
  .card--front .brand { left: 44px; top: 128px; font-size: 46px; color: var(--navy); }
  .card--front .brand__dot { width: 22px; height: 22px; }
  .card--back .brand {
    left: 0; right: 0; justify-content: center; top: 205px;
    font-size: 60px; color: var(--white);
  }
  .card--back .brand__dot { width: 28px; height: 28px; }
  .tagline {
    position: absolute; left: 45px; top: 166px; font-size: 13px; color: var(--navy);
  }
  .tagline .accent { color: var(--orange); }
  .person { position: absolute; right: 49px; top: 196px; text-align: right; }
  .person__name {
    font-family: "Catamaran", sans-serif; font-weight: 700; font-size: 23px;
    color: var(--orange); line-height: 1;
  }
  .person__role { font-size: 16px; margin-top: 5px; }
  .rule {
    position: absolute; left: 44px; top: 233px; width: 443px; height: 1.5px;
    background: var(--navy);
  }
  .rule-dots {
    position: absolute; left: 491px; top: 233px; width: 60px;
    border-top: 2px dotted var(--orange);
  }
  .contacts { position: absolute; left: 45px; top: 265px; list-style: none; }
  .contacts li {
    display: flex; align-items: center; gap: 10px;
    font-size: 16px; height: 20px; line-height: 20px;
  }
  .contacts svg { width: 15px; height: 15px; flex: none; }
  .address {
    position: absolute; right: 49px; top: 305px; text-align: right;
    font-size: 16px; line-height: 20px;
  }
  .social {
    position: absolute; left: 0; right: 0; top: 347px; text-align: center;
    font-size: 16px; color: var(--soft-white); letter-spacing: .2px;
  }
</style>
</head>
<body>
<div class="canvas">

  <section class="card card--front">
    <div class="brand"><span class="brand__dot"></span>wadol care</div>
    <p class="tagline">Professional, <span class="accent">Reliable</span>, Affordable</p>

    <div class="person">
      <div class="person__name">Tovan Brelsick</div>
      <div class="person__role">Director</div>
    </div>
    <div class="rule"></div>
    <div class="rule-dots"></div>

    <ul class="contacts">
      <li>
        <svg viewBox="0 0 16 16" aria-hidden="true"><rect x="1" y="1" width="4" height="14" rx="1" fill="var(--orange)"/><rect x="6" y="2" width="9" height="13" rx="1" fill="none" stroke="var(--orange)" stroke-width="1.6"/><rect x="8" y="4.5" width="5" height="2" fill="var(--orange)"/><rect x="8" y="8.5" width="5" height="1.5" fill="var(--orange)"/><rect x="8" y="11.5" width="5" height="1.5" fill="var(--orange)"/></svg>
        0427 31 64 92
      </li>
      <li>
        <svg viewBox="0 0 16 16" aria-hidden="true"><path d="M3.5 1.5 L6 1 L7.3 4.6 L5.6 6 C6.4 7.9 8 9.6 10 10.4 L11.4 8.7 L15 10 L14.5 12.5 C14.2 14 12.8 15 11 14.6 C6 13.5 2.5 10 1.4 5 C1 3.2 2 1.8 3.5 1.5 Z" fill="var(--orange)"/></svg>
        1300 73 29 41
      </li>
      <li>
        <svg viewBox="0 0 16 16" aria-hidden="true"><rect x="1" y="3" width="14" height="10" fill="var(--orange)"/><path d="M1 3 L8 9 L15 3 M1 13 L6 8 M15 13 L10 8" fill="none" stroke="#f4f4f4" stroke-width="1.2"/></svg>
        tovan@wadolire.com.au
      </li>
      <li>
        <svg viewBox="0 0 16 16" aria-hidden="true"><g fill="none" stroke="var(--orange)" stroke-width="1.2"><circle cx="8" cy="8" r="6.8"/><ellipse cx="8" cy="8" rx="3" ry="6.8"/><path d="M1.2 8 H14.8 M2.2 4.5 H13.8 M2.2 11.5 H13.8 M8 1.2 V14.8"/></g></svg>
        www.wadolcare.com.au
      </li>
    </ul>

    <p class="address">Here your company<br>or home address</p>
  </section>

  <section class="card card--back">
    <div class="brand"><span class="brand__dot"></span>wadol care</div>
    <p class="social">www.wadolcare.com.au/news</p>
  </section>

</div>
</body>
</html>
```